Business card for biotech sales agent

I need a logo and business card designed for my company Belunor. We work in partnership with Kestrel Group. Kestrel have developed advanced biotech. Their hand sanitiser is alcohol free and works for 24 hours on skin, even with regular hand washing. The surface sanitiser works for up to 30 days on surfaces and fabrics. Its food-safe, it's non-toxic, safe for animals and humans. The products have a very wide variety of applications: everything from agri-business, hotels, hospitality, schools, child and baby care, transport, meat processing etc.<br/>I would like my design to use blues or green-blues and communicate a bit of nano-tech but also trust and safety.<br/>I would also use the Kestrel logo on my card next to 'sales & distribution agent'

Target Market(s)

B2B, selling to FMCG and large companies such as airlines

Industry/Entity Type

Biotechnology

Contact Information for Business Card

Helen Pritch
Director

Phone: +64 22 519 3064
Email: helen@belunor.co
www.belunor.co
7 Tamsin St, Newmarket, Auckland, New Zealand 1023

Font styles to use
Sans Serif

Colors
3276b5
33b8a4
34a7d8
3176b5
ffffff

Requirements
Must have
• Not be too busy, clean space is good
• A logo styling to the word Belunor
Nice to have
• A little bit of a bio-tech image as a screen perhaps

```html
<!DOCTYPE html>
<html lang="en">
<head>
<meta charset="utf-8">
<title>Belunor – Business Card</title>
<link href="https://fonts.googleapis.com/css2?family=Montserrat:wght@300;400;600;700;800&display=swap" rel="stylesheet">
<style>
  :root {
    --bg: #e9eaec;
    --card-white: #ffffff;
    --brand-green: #8cc63f;
    --brand-blue: #4dbfe9;
    --ink: #3b3b3d;
    --ink-soft: #4a4a4c;
    --partner-navy: #1d2a5c;
  }
  * { margin: 0; padding: 0; box-sizing: border-box; }
  html, body {
    width: 1200px; height: 892px; overflow: hidden;
    background: var(--bg);
    font-family: "Montserrat", sans-serif;
  }
  .canvas {
    position: relative; width: 1200px; height: 892px;
    display: flex; align-items: center; justify-content: center; gap: 56px;
  }
  .card {
    position: relative; overflow: hidden;
    box-shadow: 0 10px 28px rgba(0,0,0,0.14);
  }

  /* Front */
  .card-front {
    width: 380px; height: 665px;
    background: var(--card-white);
    color: var(--ink);
  }
  .brand {
    position: absolute; left: 34px; top: 62px;
    display: flex; align-items: center; gap: 12px;
  }
  .brand-dot {
    width: 26px; height: 26px; border-radius: 50%;
    background: var(--brand-blue);
  }
  .brand-name {
    font-weight: 700; font-size: 33px; letter-spacing: 3px;
    color: var(--ink);
  }
  .identity {
    position: absolute; left: 172px; top: 232px;
  }
  .person-name { font-weight: 700; font-size: 20px; line-height: 1.1; }
  .person-role { font-weight: 300; font-size: 18px; line-height: 1.2; margin-bottom: 10px; }
  .partner-name {
    font-weight: 800; font-size: 15px; letter-spacing: 1px;
    color: var(--partner-navy); line-height: 1.1;
  }
  .partner-note { font-weight: 400; font-size: 10.5px; color: var(--ink-soft); }

  .divider {
    position: absolute; left: 158px; top: 385px; bottom: 0;
    width: 2px; background: var(--brand-green);
  }
  .contacts {
    position: absolute; left: 178px; top: 392px;
    list-style: none; font-size: 13px; color: var(--ink);
  }
  .contacts li { display: flex; align-items: center; gap: 10px; height: 28px; }
  .contacts svg { width: 16px; height: 16px; flex: none; }

  .accent-disc {
    position: absolute; left: 222px; top: 450px;
    width: 200px; height: 200px; border-radius: 50%;
    background: var(--brand-blue);
  }
  .address-mark {
    position: absolute; left: 34px; top: 540px;
    width: 18px; height: 18px; border-radius: 50%;
    background: var(--brand-blue);
  }
  .address {
    position: absolute; left: 30px; top: 572px;
    font-style: normal; font-size: 12px; line-height: 1.35; color: var(--ink);
  }

  /* Back */
  .card-back {
    width: 665px; height: 380px;
    background: var(--brand-green);
    color: var(--card-white);
  }
  .back-brand {
    position: absolute; left: 50%; top: 50%;
    transform: translate(-50%, -50%);
    font-weight: 700; font-size: 26px; letter-spacing: 3px;
  }
  .back-web {
    position: absolute; right: 40px; top: 50%;
    transform: translateY(-50%) rotate(-90deg);
    transform-origin: right center;
    font-weight: 400; font-size: 13px; letter-spacing: 0.5px;
    white-space: nowrap;
  }
</style>
</head>
<body>
<main class="canvas">
  <section class="card card-front">
    <div class="brand">
      <span class="brand-dot"></span>
      <span class="brand-name">BELUNOR</span>
    </div>

    <div class="identity">
      <p class="person-name">Helen Pritch</p>
      <p class="person-role">Director</p>
      <p class="partner-name">KESTREL</p>
      <p class="partner-note">sales &amp; distribution agent</p>
    </div>

    <div class="divider"></div>

    <ul class="contacts">
      <li>
        <svg viewBox="0 0 24 24" aria-hidden="true"><path fill="var(--brand-blue)" d="M6.6 10.8a15.1 15.1 0 0 0 6.6 6.6l2.2-2.2c.3-.3.7-.4 1-.2 1.1.4 2.3.6 3.6.6.6 0 1 .4 1 1V20c0 .6-.4 1-1 1A17 17 0 0 1 3 4c0-.6.4-1 1-1h3.5c.6 0 1 .4 1 1 0 1.3.2 2.5.6 3.6.1.3 0 .7-.2 1z"/></svg>
        <span>+64 22 519 3064</span>
      </li>
      <li>
        <svg viewBox="0 0 24 24" aria-hidden="true"><rect x="2.5" y="5.5" width="19" height="13" fill="none" stroke="var(--brand-blue)" stroke-width="1.5"/><path d="M2.5 5.5 12 13l9.5-7.5M2.5 18.5l7-6.5M21.5 18.5l-7-6.5" fill="none" stroke="var(--brand-blue)" stroke-width="1.5"/></svg>
        <span>helen@belunor.co</span>
      </li>
    </ul>

    <div class="accent-disc"></div>

    <span class="address-mark"></span>
    <address class="address">
      7 Tamsin St,<br>
      Larchmere,<br>
      Wendholm,<br>
      New Zealand 4017
    </address>
  </section>

  <section class="card card-back">
    <p class="back-brand">BELUNOR</p>
    <p class="back-web">www.belunor.co</p>
  </section>
</main>
</body>
</html>
```